NEW YEAR 2025 CARD

A 10 cm x 21 cm horizontal New Year card for clients and models of our 2 agencies, Pelofin and Brakovel (logo in the jobs).
Side A of the card with words and optimist creative work. The 3 (french, english, flemish) words are : ENSEMBLE TOGETHER SAMEN + creative work based on 2025 figure
Side B: the 2 logos + name of 4 people of the agency + address: Odette Rory Pierre-Gaston Anne-Sophie + Pelofin & BrakoVel - Rue des Tilleuls 47 b3 - 1360 Bruxelles - Belgique

```html
<!DOCTYPE html>
<html lang="fr">
<head>
<meta charset="utf-8">
<title>Carte de vœux 2025 — Pelofin &amp; Brakovel</title>
<link rel="stylesheet" href="https://fonts.googleapis.com/css2?family=Cutive+Mono&family=Baloo+2:wght@800&display=swap">
<style>
  :root {
    --page-bg: #ffffff;
    --card-purple: #563b9c;
    --card-purple-light: #6a4fb0;
    --card-purple-deep: #4a3190;
    --ink-light: #efeaf8;
    --ink-soft: #d9d1ee;
    --white: #ffffff;
    --title-shadow: #3a2474;
    --gold-light: #f3cf6a;
    --gold-mid: #d9a840;
    --gold-deep: #9c6b1c;
    --brand-blue: #35a9e6;
    --brand-orange: #ef7a3a;
  }
  html, body {
    margin: 0;
    padding: 0;
    width: 1200px;
    height: 1200px;
    overflow: hidden;
    background: var(--page-bg);
  }
  .greeting-card {
    position: absolute;
    left: 50px;
    top: 338px;
    width: 1100px;
    height: 524px;
    overflow: hidden;
    background:
      radial-gradient(ellipse at 75% 20%, var(--card-purple-light) 0%, transparent 60%),
      linear-gradient(135deg, var(--card-purple-deep) 0%, var(--card-purple) 55%, var(--card-purple) 100%);
    font-family: "Cutive Mono", monospace;
  }
  .hanging-decor {
    position: absolute;
    left: 40px;
    top: 0;
    width: 300px;
    height: 470px;
    background: radial-gradient(ellipse at 50% 55%, rgba(243, 207, 106, 0.18) 0%, transparent 70%);
  }
  .year-figure {
    position: absolute;
    left: 78px;
    top: 70px;
    margin: 0;
    font-family: "Baloo 2", sans-serif;
    font-weight: 800;
    font-size: 210px;
    line-height: 0.82;
    color: var(--gold-light);
    text-shadow: 4px 4px 0 var(--gold-mid), 8px 8px 0 var(--gold-deep), 10px 14px 18px var(--title-shadow);
  }
  .year-row { display: block; white-space: nowrap; }
  .year-digit { display: inline-block; }
  .year-digit-offset { position: relative; top: 48px; margin-left: -8px; }
  .motto {
    position: absolute;
    margin: 0;
    font-family: "Baloo 2", sans-serif;
    font-weight: 800;
    color: var(--white);
    line-height: 1;
    white-space: nowrap;
    text-shadow: 0 3px 0 var(--ink-soft), 0 8px 14px var(--title-shadow);
  }
  .motto-fr { left: 410px; top: 126px; font-size: 46px; letter-spacing: 1px; }
  .motto-en { left: 372px; top: 178px; font-size: 94px; letter-spacing: -1px; }
  .motto-nl { left: 505px; top: 282px; font-size: 50px; letter-spacing: 1px; }
  .team-names {
    position: absolute;
    right: 63px;
    top: 96px;
    margin: 0;
    text-align: right;
    font-size: 24px;
    line-height: 33px;
    color: var(--ink-light);
  }
  .team-line { display: block; white-space: nowrap; }
  .agency-brands {
    position: absolute;
    right: 63px;
    top: 272px;
    display: flex;
    gap: 26px;
  }
  .agency-name {
    font-size: 26px;
    letter-spacing: 0.5px;
    white-space: nowrap;
  }
  .agency-pelofin { color: var(--brand-blue); }
  .agency-brakovel { color: var(--brand-orange); }
  .agency-address {
    position: absolute;
    right: 63px;
    top: 452px;
    margin: 0;
    font-size: 17px;
    color: var(--ink-soft);
    white-space: nowrap;
  }
</style>
</head>
<body>
  <main class="greeting-card">
    <div class="hanging-decor" role="img" aria-label="Gold strings with hanging red baubles and gold stars"></div>

    <p class="year-figure" aria-label="2025">
      <span class="year-row"><span class="year-digit">2</span><span class="year-digit year-digit-offset">0</span></span>
      <span class="year-row"><span class="year-digit">2</span><span class="year-digit year-digit-offset">5</span></span>
    </p>

    <p class="motto motto-fr">ENSEMBLE</p>
    <p class="motto motto-en">Together</p>
    <p class="motto motto-nl">SAMEN</p>

    <p class="team-names">
      <span class="team-line">Odette Rory</span>
      <span class="team-line">Pierre&#8209;Gaston</span>
      <span class="team-line">Anne&#8209;Sophie</span>
    </p>

    <div class="agency-brands">
      <span class="agency-name agency-pelofin">Pelofin</span>
      <span class="agency-name agency-brakovel">Brakovel</span>
    </div>

    <p class="agency-address">Rue des Tilleuls 47 b3 | 1360 Bruxelles | Belgique</p>
  </main>
</body>
</html>
```